Brightvale Crew Word Press Website

We need a graphical, fun website that conveys our messaging of providing the Best-In-Class Signature Marketing System for Mortgage Loan Officers and Realtors. Our system uses AI and Predictive Analysis to uncover the 'Gold' hidden in contact databases. The 'Gold' is defined as people who are in the market or likely to be in the market soon. We place that 'Gold' in the form of Contact Name, Address, Phone and Email on a Daily To Do List detailing what type of contact should be made.

Target Market(s)

Mortgage Loan Officers and Realtors

Industry/Entity Type

Mortgage & Real Estate

Coding

Coded - Design and coding required

Number of Pages Required

5+ page

Requirements
Must have
• I like the look of this site- https://www.homeloanpromostudio.example/
Nice to have
• Please create a flow that is similar to https://www.homeloanpromostudio.example/, but better, more dynamic. Site must be responsive and mobile friendly. Site will have embedded videos. Site need to convey a message of hope, imagination, innovation, results oriented, better than the rest, victory!
Should not have
• Nothing cheesy or low class.

```html
<!DOCTYPE html>
<html lang="en">
<head>
<meta charset="utf-8">
<title>Brightvale Crew</title>
<link href="https://fonts.googleapis.com/css2?family=Poppins:wght@400;500;600;700&display=swap" rel="stylesheet">
<style>
:root{
  --blue:#1552dc;
  --blue-bright:#1a7de8;
  --gold:#dcb340;
  --gold-deep:#d3a62a;
  --gold-soft:#f2d774;
  --ink:#1b1b1b;
  --muted:#6d6d6d;
  --sky:#eaf6fc;
  --white:#ffffff;
  --black:#050505;
  --violet:#5f57e0;
  --violet-soft:#9d97f2;
  --lilac:#d9d6fa;
}
*{box-sizing:border-box;margin:0;padding:0}
html,body{width:1200px;height:3654px;overflow:hidden;background:var(--white)}
body{font-family:"Poppins",sans-serif;color:var(--ink)}
.page{position:relative;width:1200px;height:3654px;overflow:hidden}
.abs{position:absolute}
.hero-bg{left:0;top:0;width:1200px;height:1337px;background:var(--sky)}
.top-line{left:0;top:0;width:1200px;height:5px;background:linear-gradient(90deg,var(--blue),var(--blue-bright))}
.hero-wave{left:0;top:0}
.brand{left:99px;top:58px;width:180px;text-align:center}
.brand-dot{width:46px;height:46px;border-radius:50%;background:var(--blue);margin:0 auto 12px}
.brand-name{font-weight:700;font-size:26px;line-height:30px;color:var(--gold);letter-spacing:1px}
.nav{top:46px;height:24px;font-size:14px;font-weight:600;color:var(--white);letter-spacing:.3px}
.btn{display:flex;align-items:center;justify-content:center;font-weight:600;color:var(--white);font-size:14px;letter-spacing:.3px}
.btn-gold{background:var(--gold)}
.btn-blue{background:linear-gradient(90deg,var(--blue-bright),var(--blue))}
.eyebrow{font-weight:600;color:var(--gold);letter-spacing:.3px}
.title{font-weight:700;color:var(--blue);letter-spacing:.5px;white-space:nowrap}
.body{font-size:11.5px;line-height:20.6px;color:var(--muted)}
.art{border-radius:28px;box-shadow:0 18px 40px rgba(80,70,200,.18)}
.art-violet{background:linear-gradient(145deg,var(--violet-soft) 0%,var(--violet) 55%,#4038c8 100%)}
.art-violet-gold{background:linear-gradient(145deg,var(--violet-soft) 0%,var(--violet) 50%,var(--gold) 100%)}
.art-gold{background:linear-gradient(145deg,var(--gold-soft) 0%,var(--gold) 55%,var(--violet) 100%)}
.art-blue{background:linear-gradient(145deg,#7db2f2 0%,var(--blue-bright) 55%,var(--violet) 100%)}
.service{width:300px;text-align:center}
.service-art{width:250px;height:200px;margin:10px auto 0}
.service-title{font-weight:700;font-size:18px;color:var(--ink);white-space:nowrap}
.service-text{font-size:11.5px;line-height:20.6px;color:var(--muted);width:290px;margin:8px auto 0}
.service-link{display:inline-block;margin-top:6px;font-weight:600;font-size:14px;color:var(--gold);border-bottom:1px solid var(--gold);line-height:20px}
.contact-band{left:0;top:2593px;width:1200px;height:736px;background:linear-gradient(120deg,var(--gold-deep),#f0cf5a 55%,var(--gold-deep))}
.contact-card{left:725px;top:2654px;width:400px;height:615px;background:var(--white)}
.field{left:39px;width:323px;height:51px;border:1px solid #c9c9c9;font-size:13px;color:#555;padding:0 24px;display:flex;align-items:center}
.footer{left:0;top:3329px;width:1200px;height:325px;background:var(--black)}
.foot-link{top:3557px;font-size:14px;font-weight:500;color:var(--white)}
</style>
</head>
<body>
<div class="page">

  <div class="abs hero-bg"></div>
  <svg class="abs hero-wave" width="1200" height="520" viewBox="0 0 1200 520" aria-hidden="true">
    <defs>
      <linearGradient id="waveFill" x1="0" y1="0" x2="1" y2="1">
        <stop offset="0" stop-color="#1a7de8"/>
        <stop offset="1" stop-color="#1548d8"/>
      </linearGradient>
    </defs>
    <path d="M407 0 C 405 120, 470 200, 640 250 C 820 300, 1100 310, 1200 505 L1200 0 Z" fill="url(#waveFill)"/>
  </svg>
  <div class="abs top-line"></div>

  <div class="abs brand">
    <div class="brand-dot"></div>
    <div class="brand-name">BRIGHTVALE<br>CREW</div>
  </div>

  <div class="abs nav" style="left:468px">HOME</div>
  <div class="abs nav" style="left:576px">ABOUT US</div>
  <div class="abs nav" style="left:715px">SERVICES</div>
  <div class="abs nav" style="left:849px">REVIEWS</div>
  <div class="abs btn btn-gold" style="left:959px;top:37px;width:142px;height:42px">GET A QUOTE</div>

  <div class="abs art art-violet-gold" role="img" aria-label="Isometric illustration of a couple, an agent with keys, a contract and a house for sale with coins and a calculator" style="left:620px;top:120px;width:470px;height:560px;border-radius:40px"></div>

  <div class="abs eyebrow" style="left:99px;top:326px;font-size:25px">WELCOME TO</div>
  <div class="abs title" style="left:97px;top:354px;font-size:50px;line-height:64px">BRIGHTVALE CREW</div>
  <p class="abs body" style="left:99px;top:431px;width:460px">Lorem ipsum dolor sit amet, consectetur adipiscing elit, sed do eiusmod tempor incididunt ut labore et dolore magna aliqua. Quis ipsum suspendisse ultrices gravida. Risus</p>
  <div class="abs btn btn-gold" style="left:99px;top:516px;width:251px;height:43px">SCHEDULE CONSULTATION</div>

  <div class="abs art art-violet" role="img" aria-label="Isometric illustration of a hand holding a house with keys, a man with a card, a 24/7 clock and a check badge" style="left:99px;top:790px;width:540px;height:460px;border-radius:40px"></div>

  <div class="abs eyebrow" style="left:681px;top:843px;font-size:17px">GET MORE TRAFFIC.</div>
  <div class="abs title" style="left:681px;top:868px;font-size:34px;line-height:46px">GET MORE LOANS!</div>
  <p class="abs body" style="left:681px;top:929px;width:420px">Lorem ipsum dolor sit amet, consectetur adipiscing elit, sed do eiusmod tempor incididunt ut labore et dolore magna aliqua. Quis ipsum suspendisse ultrices gravida. Risus commodo viverra maecenas accumsan lacus vel facilisis.</p>
  <p class="abs body" style="left:681px;top:1032px;width:420px">Contrary to popular belief, Lorem Ipsum is not simply random text. It has roots in a piece of classical Latin literature from 45 BC, making it over 2000 years old. Daniel Ashcombe, a Latin professor at Fairholt College in Virginia, looked up one of the more obscure Latin words, consectetur, from a Lorem Ipsum passage, and</p>
  <div class="abs btn btn-gold" style="left:682px;top:1163px;width:203px;height:43px">SCHEDULE A CALL</div>

  <div class="abs eyebrow" style="left:0;top:1416px;width:1200px;text-align:center;font-size:17px">SERVICES</div>
  <div class="abs title" style="left:0;top:1442px;width:1200px;text-align:center;font-size:34px;line-height:46px">WE’VE GOT YOU COVERED</div>

  <div class="abs service" style="left:118px;top:1553px">
    <div class="service-art art art-violet" role="img" aria-label="Isometric house on a blueprint with coins and keys"></div>
    <div class="service-title" style="margin-top:62px">CONTENT MARKETING</div>
    <div class="service-text">Lorem ipsum dolor sit amet, consectetur adipiscing elit, sed do eiusmod tempor incididunt ut labore et dolore magna aliqua. Quis ipsum suspendisse ultrices gravida. Risus commodo</div>
    <div class="service-link">LEARN MORE</div>
  </div>
  <div class="abs service" style="left:464px;top:1553px">
    <div class="service-art art art-violet" role="img" aria-label="Isometric house with a laptop, rating stars and shield"></div>
    <div class="service-title" style="margin-top:62px">BRAND DESIGN &amp; STRATEGY</div>
    <div class="service-text">Lorem ipsum dolor sit amet, consectetur adipiscing elit, sed do eiusmod tempor incididunt ut labore et dolore magna aliqua. Quis ipsum suspendisse ultrices gravida. Risus commodo</div>
    <div class="service-link">LEARN MORE</div>
  </div>
  <div class="abs service" style="left:812px;top:1553px">
    <div class="service-art art art-violet-gold" role="img" aria-label="Isometric man placing a coin into a house beside a contract"></div>
    <div class="service-title" style="margin-top:62px">SOCIAL MEDIA MANAGEMENT</div>
    <div class="service-text">Lorem ipsum dolor sit amet, consectetur adipiscing elit, sed do eiusmod tempor incididunt ut labore et dolore magna aliqua. Quis ipsum suspendisse ultrices gravida. Risus commodo</div>
    <div class="service-link">LEARN MORE</div>
  </div>

  <div class="abs service" style="left:118px;top:2010px">
    <div class="service-art art art-blue" role="img" aria-label="Isometric house with people, cards and a checklist"></div>
    <div class="service-title" style="margin-top:48px">WEBSITE DEVELOPMENT</div>
    <div class="service-text">Lorem ipsum dolor sit amet, consectetur adipiscing elit, sed do eiusmod tempor incididunt ut labore et dolore magna aliqua. Quis ipsum suspendisse ultrices gravida. Risus commodo</div>
    <div class="service-link">LEARN MORE</div>
  </div>
  <div class="abs service" style="left:464px;top:2010px">
    <div class="service-art art art-gold" role="img" aria-label="Isometric credit score gauge with calculator and coins"></div>
    <div class="service-title" style="margin-top:48px">SEARCH ENGINE OPTIMIZATION</div>
    <div class="service-text">Lorem ipsum dolor sit amet, consectetur adipiscing elit, sed do eiusmod tempor incididunt ut labore et dolore magna aliqua. Quis ipsum suspendisse ultrices gravida. Risus commodo</div>
    <div class="service-link">LEARN MORE</div>
  </div>
  <div class="abs service" style="left:812px;top:2010px">
    <div class="service-art art art-violet-gold" role="img" aria-label="Isometric hands passing a key above a house with coins"></div>
    <div class="service-title" style="margin-top:48px">MORTGAGE CHATBOT</div>
    <div class="service-text">Lorem ipsum dolor sit amet, consectetur adipiscing elit, sed do eiusmod tempor incididunt ut labore et dolore magna aliqua. Quis ipsum suspendisse ultrices gravida. Risus commodo</div>
    <div class="service-link">LEARN MORE</div>
  </div>

  <div class="abs btn btn-gold" style="left:380px;top:2471px;width:203px;height:42px">VIEW ALL SERVICES</div>
  <div class="abs btn btn-blue" style="left:617px;top:2471px;width:203px;height:42px">SCHEDULE A CALL</div>

  <div class="abs contact-band"></div>
  <div class="abs art" role="img" aria-label="Isometric blue house on a tablet with a sale tag, contract, calculator and gold coins" style="left:30px;top:2700px;width:640px;height:540px;border-radius:40px;background:linear-gradient(150deg,#8d93ec 0%,#4f56d8 60%,#3a3fb8 100%)"></div>

  <div class="abs contact-card">
    <div class="abs eyebrow" style="left:39px;top:38px;font-size:17px">LET’S GET STARTED</div>
    <div class="abs title" style="left:39px;top:62px;font-size:33px;line-height:46px">GET IN TOUCH</div>
    <div class="abs field" style="top:127px">Full Name :</div>
    <div class="abs field" style="top:195px">Email Addres :</div>
    <div class="abs field" style="top:263px">Phone Number :</div>
    <div class="abs field" style="top:330px;justify-content:space-between">Choose the Service
      <svg width="16" height="10" viewBox="0 0 16 10" aria-hidden="true"><path d="M1 1 L8 8 L15 1" fill="none" stroke="#555" stroke-width="1.6"/></svg>
    </div>
    <div class="abs field" style="top:398px;height:104px;align-items:flex-start;padding-top:16px">Your Messages Goes Here....</div>
    <div class="abs btn btn-blue" style="left:39px;top:523px;width:323px;height:51px">SEND REQUEST</div>
  </div>

  <div class="abs footer"></div>
  <div class="abs" style="left:0;top:3380px;width:1200px;text-align:center">
    <div style="width:50px;height:50px;border-radius:50%;background:var(--white);margin:0 auto 14px"></div>
    <div style="font-weight:700;font-size:30px;line-height:34px;color:var(--white);letter-spacing:1px">BRIGHTVALE<br>CREW</div>
  </div>
  <div class="abs foot-link" style="left:172px">HOME</div>
  <div class="abs foot-link" style="left:294px">ABOUT US</div>
  <div class="abs foot-link" style="left:445px">SERVICES</div>
  <div class="abs foot-link" style="left:592px">REVIEWS</div>
  <div class="abs foot-link" style="left:734px">PRIVACY POLICY</div>
  <div class="abs foot-link" style="left:931px">CONTACT US</div>
  <div class="abs" style="left:0;top:3598px;width:1200px;text-align:center;font-size:13px;color:var(--white)">© 2022 Brightvale Crew . All Rights Reserved.</div>

  <svg class="abs" style="left:1086px;top:3488px" width="54" height="54" viewBox="0 0 54 54" aria-label="Chat">
    <circle cx="27" cy="27" r="26" fill="#1a7de8"/>
    <path d="M17 20 h16 a3 3 0 0 1 3 3 v8 a3 3 0 0 1 -3 3 h-10 l-5 4 v-4 h-1 a3 3 0 0 1 -3 -3 v-8 a3 3 0 0 1 3 -3 z" fill="none" stroke="#fff" stroke-width="2"/>
    <line x1="20" y1="25" x2="30" y2="25" stroke="#fff" stroke-width="2"/>
    <line x1="20" y1="29" x2="27" y2="29" stroke="#fff" stroke-width="2"/>
  </svg>

</div>
</body>
</html>
```